Fish guide business card

Buisiness card

Target Market(s)

Visitors to Campbell River Bc wanting to catch fish in the ocean and have a memorable adventure fun filled day

Industry/Entity Type

Tourism

Contact Information for Business Card

Phone number 250 318 two cards Ray 250 318 7262 other card Lou 250 6093714 both have email info@lwgullrocktours.com and website www.lwgullrocktours.com

Requirements
Must have
• Email, website , name , phone , logo , Campbell River BC
Nice to have
• Uploaded pictures have boat and man with fish picture

```html
<!DOCTYPE html>
<html lang="en">
<head>
<meta charset="utf-8">
<title>LW Gull Rock Tours – Business Card</title>
<link href="https://fonts.googleapis.com/css2?family=Montserrat:wght@400;700;800&display=swap" rel="stylesheet">
<style>
  :root {
    --navy: #2b2478;
    --navy-deep: #26206d;
    --navy-gloss: #3a3290;
    --ink: #2f2a7a;
    --white: #ffffff;
    --page: #e9e9ec;
    --sea: #4f6a8a;
    --sea-light: #9fb3c8;
  }
  * { box-sizing: border-box; margin: 0; padding: 0; }
  html, body { width: 1200px; height: 913px; overflow: hidden; }
  body {
    background: var(--page);
    font-family: "Montserrat", Arial, sans-serif;
    position: relative;
  }
  .card {
    position: absolute;
    width: 620px;
    height: 354px;
    border-radius: 22px;
    overflow: hidden;
    box-shadow: 0 10px 30px rgba(0,0,0,.18);
  }
  /* Back of card */
  .card-back {
    left: 80px;
    top: 70px;
    background: var(--navy-deep);
    display: flex;
    align-items: center;
    justify-content: center;
  }
  .back-mark {
    display: flex;
    align-items: center;
    gap: 16px;
    color: var(--navy-gloss);
    font-weight: 800;
    font-size: 34px;
    letter-spacing: .5px;
  }
  .back-mark .dot {
    width: 34px; height: 34px; border-radius: 50%;
    background: var(--navy-gloss);
  }
  /* Front of card */
  .card-front {
    left: 500px;
    top: 490px;
    background: var(--white);
  }
  .photo {
    position: absolute;
    right: 0; top: 0;
    width: 360px; height: 100%;
    background:
      linear-gradient(90deg, var(--white) 0%, rgba(255,255,255,0) 35%),
      linear-gradient(180deg, var(--sea-light) 0%, var(--sea) 35%, #5d6e62 70%, #8a7b62 100%);
  }
  .brand {
    position: absolute;
    left: 34px; top: 40px;
    display: flex;
    align-items: center;
    gap: 12px;
    color: var(--navy);
    font-weight: 800;
    font-size: 22px;
  }
  .brand .dot {
    width: 24px; height: 24px; border-radius: 50%;
    background: var(--navy);
  }
  .contact {
    position: absolute;
    left: 40px; bottom: 34px;
    color: var(--ink);
  }
  .contact .name {
    font-weight: 800;
    font-size: 28px;
    margin-bottom: 14px;
    text-transform: uppercase;
  }
  .contact ul { list-style: none; }
  .contact li {
    display: flex;
    align-items: center;
    gap: 10px;
    font-size: 19px;
    line-height: 1.45;
  }
  .contact svg { width: 16px; height: 16px; fill: var(--navy); flex: none; }
</style>
</head>
<body>
  <section class="card card-back">
    <div class="back-mark"><span class="dot"></span>LW Gull Rock Tours</div>
  </section>

  <section class="card card-front">
    <div class="photo" role="img" aria-label="Photo of a fishing guide on a boat holding a large salmon, with ocean and mountains behind"></div>
    <div class="brand"><span class="dot"></span>LW Gull Rock Tours</div>
    <div class="contact">
      <p class="name">Lou</p>
      <ul>
        <li>
          <svg viewBox="0 0 24 24"><path d="M6.6 10.8a15.1 15.1 0 0 0 6.6 6.6l2.2-2.2a1 1 0 0 1 1-.25 11.4 11.4 0 0 0 3.6.57 1 1 0 0 1 1 1V20a1 1 0 0 1-1 1A17 17 0 0 1 3 4a1 1 0 0 1 1-1h3.5a1 1 0 0 1 1 1c0 1.25.2 2.45.57 3.57a1 1 0 0 1-.25 1z"/></svg>
          250 6093714
        </li>
        <li>
          <svg viewBox="0 0 24 24"><path d="M2 5h20v14H2z M2 5l10 8 10-8" /></svg>
          info@lwgullrocktours.com
        </li>
        <li>
          <svg viewBox="0 0 24 24"><circle cx="12" cy="12" r="10"/><path d="M2 12h20M12 2c3 3 3 17 0 20M12 2c-3 3-3 17 0 20" stroke="#fff" stroke-width="1.5" fill="none"/></svg>
          www.lwgullrocktours.com
        </li>
      </ul>
    </div>
  </section>
</body>
</html>
```